Keystone Subsurface Mapping
Thank you all for submitting designs. You guys make it really tough to pick a design they were all good.
Thanks again.
I just added more funds to the project. I will need a word template for the letterhead.
I do not need any business card designs they are all good. Just looking at matching stationery now.
Thank you.
Please include a matching letterhead. I will add more funds to the project for stationery.
Could you include stationery.
I have attached our logo and sample biz card front and back.
Use tag line in front and list of service in back of card.
Only use contact information in the brief.

```html
<!DOCTYPE html>
<html lang="en">
<head>
<meta charset="utf-8">
<title>Keystone Subsurface Mapping – Stationery</title>
<link href="https://fonts.googleapis.com/css2?family=Oswald:wght@600&family=Open+Sans:wght@400;600;700&display=swap" rel="stylesheet">
<style>
  :root{
    --bg:#e4e2df;
    --paper:#ffffff;
    --ink:#1d1d1d;
    --ink-soft:#555555;
    --orange:#f0a000;
    --yellow:#f6c41c;
    --rule:#cfcfcf;
    --ghost-a:#f3efe6;
    --ghost-b:#e6dfcf;
  }
  *{box-sizing:border-box;margin:0;padding:0}
  html,body{width:1200px;height:758px;overflow:hidden}
  body{background:var(--bg);font-family:"Open Sans",Arial,sans-serif;color:var(--ink);position:relative}
  .sheet{position:absolute;background:var(--paper);box-shadow:0 2px 8px rgba(0,0,0,.18);overflow:hidden}
  .swoosh{position:absolute;left:0;bottom:0;width:100%}
  .brand{display:flex;align-items:center;gap:5px}
  .brand-dot{width:12px;height:12px;background:var(--orange)}
  .brand-name{font-family:"Oswald",Arial,sans-serif;font-weight:600;color:var(--ink);letter-spacing:1px;font-size:16px;line-height:1}
  .on-dark .brand-name{color:var(--paper)}
  .tagline{position:absolute;right:12px;color:var(--paper);font-size:6.5px;line-height:1.35;text-align:right;font-weight:600}
  .ghost{position:absolute;left:0;right:0;background:linear-gradient(180deg,var(--paper),var(--ghost-a) 40%,var(--ghost-b))}
  .tiny{font-size:5px;line-height:1.4;color:var(--ink-soft)}

  /* business cards */
  .card{width:300px;height:172px}
  .card-back{left:40px;top:46px;background:var(--ink)}
  .card-back .brand{position:absolute;left:26px;top:58px}
  .card-back .brand-name{font-size:26px}
  .card-back .brand-dot{width:20px;height:20px}
  .card-back .company{position:absolute;right:20px;top:62px;text-align:right;color:var(--paper);font-size:9px;font-weight:700;width:130px;line-height:1.3}
  .card-back .company span{display:block;color:var(--orange);font-weight:600;font-size:7px;margin-top:4px}
  .card-front{left:40px;top:238px}
  .card-front .brand{position:absolute;left:22px;top:22px}
  .card-front .contact{position:absolute;right:20px;top:22px;text-align:right}
  .card-front .person{font-size:11px;font-weight:700}
  .card-front .role{font-size:7px;color:var(--orange);font-weight:600;margin-bottom:8px}
  .card-front .line{font-size:7px;color:var(--ink-soft);line-height:1.55}
  .card-front .tagline{bottom:7px;font-size:6px}

  /* letterhead + fax */
  .page{width:300px;height:388px;top:40px}
  .letterhead{left:410px}
  .fax{left:750px}
  .page .brand{position:absolute;left:22px;top:22px}
  .page .sender{position:absolute;right:20px;top:22px;text-align:right;width:120px}
  .page .ghost{bottom:40px;height:130px}
  .page .tagline{bottom:10px}
  .fax-title{position:absolute;right:20px;top:62px;font-family:"Oswald",Arial,sans-serif;font-weight:600;font-size:16px;letter-spacing:1px}
  .fax-fields{position:absolute;left:22px;right:20px;top:88px;display:grid;grid-template-columns:1fr 1fr;column-gap:18px;row-gap:6px}
  .field{display:flex;align-items:flex-end;gap:4px;font-size:5.5px;color:var(--ink-soft)}
  .field i{flex:1;border-bottom:1px solid var(--rule);height:6px}
  .fax-checks{position:absolute;left:22px;right:20px;top:140px;display:flex;justify-content:space-between;border-top:1px solid var(--rule);border-bottom:1px solid var(--rule);padding:5px 0}
  .check{display:flex;align-items:center;gap:3px;font-size:5px;color:var(--ink-soft)}
  .check b{width:5px;height:5px;border:1px solid var(--ink-soft)}
  .fax-comments{position:absolute;left:22px;top:160px;font-size:5.5px;color:var(--ink-soft)}

  /* compliment slip */
  .slip{left:40px;top:478px;width:300px;height:141px}
  .slip .brand{position:absolute;left:20px;top:16px}
  .slip .sender{position:absolute;right:16px;top:16px;text-align:right;width:100px}
  .slip .ghost{bottom:30px;height:70px}
  .slip .tagline{bottom:6px}

  /* envelopes */
  .envelope{top:500px;width:240px;height:104px}
  .env-front{left:400px}
  .env-yellow{left:660px}
  .env-black{left:920px}
  .env-front .brand{position:absolute;left:12px;top:10px}
  .env-front .brand-name{font-size:12px}
  .env-front .brand-dot{width:9px;height:9px}
  .env-front .sender{position:absolute;left:12px;top:28px;width:110px}
  .flap{position:absolute;left:0;top:0;width:100%;height:60px}
  .flap-brand{position:absolute;left:50%;top:30px;transform:translateX(-50%)}
  .flap-brand .brand-name{font-size:10px}
  .flap-brand .brand-dot{width:7px;height:7px}
</style>
</head>
<body>

<svg width="0" height="0" style="position:absolute" aria-hidden="true">
  <symbol id="footer-swoosh" viewBox="0 0 300 60" preserveAspectRatio="none">
    <path d="M0 26 C90 4 170 44 300 14 L300 60 L0 60 Z" fill="#1d1d1d"/>
    <path d="M0 20 C90 -2 170 38 300 8" fill="none" stroke="#f0a000" stroke-width="3"/>
  </symbol>
  <symbol id="card-curve" viewBox="0 0 300 172" preserveAspectRatio="none">
    <path d="M0 120 C90 95 180 150 300 110" fill="none" stroke="#f0a000" stroke-width="3"/>
  </symbol>
</svg>

<!-- Business card, back -->
<section class="sheet card card-back on-dark" aria-label="Business card back">
  <svg class="swoosh" width="300" height="172" viewBox="0 0 300 172" preserveAspectRatio="none"><use href="#card-curve"/></svg>
  <div class="brand"><span class="brand-dot"></span><span class="brand-name">KSM</span></div>
  <p class="company">Keystone Subsurface Mapping<span>Sub-surface Utility Locating</span></p>
</section>

<!-- Business card, front -->
<section class="sheet card card-front" aria-label="Business card front">
  <div class="brand"><span class="brand-dot"></span><span class="brand-name">KSM</span></div>
  <div class="contact">
    <p class="person">Tom A. MacPhee</p>
    <p class="role">Owner / Lead Locator</p>
    <p class="line">T (555) 014-2287</p>
    <p class="line">C (555) 014-9930</p>
    <p class="line">tmacphee@keystonesm.com</p>
    <p class="line">www.keystonesm.com</p>
  </div>
  <svg class="swoosh" width="300" height="46" viewBox="0 0 300 60" preserveAspectRatio="none"><use href="#footer-swoosh"/></svg>
  <p class="tagline">Specializing in all Sub-surface<br>Utility Locating, GPR and Concrete Scans</p>
</section>

<!-- Letterhead -->
<section class="sheet page letterhead" aria-label="Letterhead">
  <div class="brand"><span class="brand-dot"></span><span class="brand-name">KSM</span></div>
  <div class="sender tiny">
    <p>418 Quarry Ridge Road</p>
    <p>Brookfield, CT 06804</p>
    <p>T (555) 014-2287</p>
    <p>tmacphee@keystonesm.com</p>
  </div>
  <div class="ghost" role="img" aria-label="Faint photo of a utility locating crew at work"></div>
  <svg class="swoosh" width="300" height="60" viewBox="0 0 300 60" preserveAspectRatio="none"><use href="#footer-swoosh"/></svg>
  <p class="tagline">Specializing in all Sub-surface<br>Utility Locating, GPR and Concrete Scans</p>
</section>

<!-- Fax sheet -->
<section class="sheet page fax" aria-label="Fax cover sheet">
  <div class="brand"><span class="brand-dot"></span><span class="brand-name">KSM</span></div>
  <div class="sender tiny">
    <p>418 Quarry Ridge Road</p>
    <p>Brookfield, CT 06804</p>
    <p>T (555) 014-2287</p>
    <p>tmacphee@keystonesm.com</p>
  </div>
  <h1 class="fax-title">FAX</h1>
  <div class="fax-fields">
    <p class="field">To:<i></i></p><p class="field">From:<i></i></p>
    <p class="field">Fax:<i></i></p><p class="field">Pages:<i></i></p>
    <p class="field">Phone:<i></i></p><p class="field">Date:<i></i></p>
    <p class="field">Re:<i></i></p><p class="field">CC:<i></i></p>
  </div>
  <div class="fax-checks">
    <span class="check"><b></b>Urgent</span>
    <span class="check"><b></b>For Review</span>
    <span class="check"><b></b>Please Comment</span>
    <span class="check"><b></b>Please Reply</span>
    <span class="check"><b></b>Please Recycle</span>
  </div>
  <p class="fax-comments">Comments:</p>
  <div class="ghost" role="img" aria-label="Faint photo of a utility locating crew at work"></div>
  <svg class="swoosh" width="300" height="60" viewBox="0 0 300 60" preserveAspectRatio="none"><use href="#footer-swoosh"/></svg>
  <p class="tagline">Specializing in all Sub-surface<br>Utility Locating, GPR and Concrete Scans</p>
</section>

<!-- Compliment slip -->
<section class="sheet slip" aria-label="Compliment slip">
  <div class="brand"><span class="brand-dot"></span><span class="brand-name">KSM</span></div>
  <div class="sender tiny">
    <p>418 Quarry Ridge Road</p>
    <p>Brookfield, CT 06804</p>
    <p>T (555) 014-2287</p>
  </div>
  <div class="ghost" role="img" aria-label="Faint photo of a utility locating crew at work"></div>
  <svg class="swoosh" width="300" height="44" viewBox="0 0 300 60" preserveAspectRatio="none"><use href="#footer-swoosh"/></svg>
  <p class="tagline">Specializing in all Sub-surface<br>Utility Locating, GPR and Concrete Scans</p>
</section>

<!-- Envelope, front -->
<section class="sheet envelope env-front" aria-label="Envelope front">
  <div class="brand"><span class="brand-dot"></span><span class="brand-name">KSM</span></div>
  <div class="sender tiny">
    <p>418 Quarry Ridge Road</p>
    <p>Brookfield, CT 06804</p>
  </div>
</section>

<!-- Envelope, back with yellow flap -->
<section class="sheet envelope env-yellow" aria-label="Envelope back, yellow flap">
  <svg class="flap" viewBox="0 0 240 60" preserveAspectRatio="none" aria-hidden="true">
    <path d="M0 0 H240 V8 C180 12 150 58 120 58 C90 58 60 12 0 8 Z" fill="#f6c41c"/>
  </svg>
  <div class="brand flap-brand"><span class="brand-dot"></span><span class="brand-name">KSM</span></div>
</section>

<!-- Envelope, back with black flap -->
<section class="sheet envelope env-black" aria-label="Envelope back, black flap">
  <svg class="flap" viewBox="0 0 240 60" preserveAspectRatio="none" aria-hidden="true">
    <path d="M0 0 H240 V8 C180 12 150 58 120 58 C90 58 60 12 0 8 Z" fill="#1d1d1d"/>
  </svg>
  <div class="brand flap-brand on-dark"><span class="brand-dot"></span><span class="brand-name">KSM</span></div>
</section>

</body>
</html>
```